OTT TV and VOD Service Website (like Vexamo.tv ; Brindo etc.)

Site will be used as a marketing page integrated with subscription processing (Quellpay). Looking for someone with solid experience in designing video content driven sites. For the looks; clean, modern, black background with rich "popping" VOD and live TV channel titles.

Target Market(s)

Video-on-demand and international live TV channel subscribers in Asia

Coding

Number of Pages Required

Font styles to use
Other font styles liked:

Requirements
Must have
• Start with an awesome looking "coming soon" page, featuring a logo on black background with video (i.e. a movie trailers) playing in the background. This page should also have an understated "about" link and an email "contact" form.
Site: Scrollable interfaces: Service / Live Channels / VOD / Subscribe.
Contrasting backgrounds as the page is being scrolled. Black as a dominating background color. See Vexamo.tv site for inspiration
There will be contact form (Register)
Nice to have
• Dynamic video background on the home page (trailer / title / channel promo)
Clear interface separation between live TV channels and VOD
Should not have
• Typical template looking scrolling site with boring icons and

```html
<!DOCTYPE html>
<html lang="en">
<head>
<meta charset="utf-8">
<title>Lumora.TV — Coming Soon</title>
<link rel="stylesheet" href="https://fonts.googleapis.com/css2?family=Montserrat:wght@500;600;700&family=Roboto:wght@400;500&display=swap">
<style>
:root{
  --blue:#1e8fd5;
  --green:#8dc63f;
  --ink:#2b2b2b;
  --muted:#444;
  --grey-band:#ebebeb;
  --plan-bg:#e9e9e9;
  --black:#000;
  --bar:#161616;
  --white:#fff;
}
*{box-sizing:border-box;margin:0;padding:0}
html,body{width:1200px;height:3722px;overflow:hidden}
body{font-family:Roboto,Arial,sans-serif;color:var(--ink);background:var(--white);position:relative}
h1,h2,h3,h4,.brand,.nav a,.btn{font-family:Montserrat,Arial,sans-serif}

/* hero */
.hero{position:absolute;left:0;top:0;width:1200px;height:640px;overflow:hidden}
.hero-photo{position:absolute;inset:0;background:radial-gradient(ellipse at 80% 20%,#4a5a6e 0%,transparent 40%),radial-gradient(ellipse at 30% 60%,#3a2a22 0%,transparent 50%),linear-gradient(180deg,#1b1a1d 0%,#25211f 60%,#2e2a26 100%)}
.brand{position:absolute;font-weight:600;font-size:31px;color:var(--blue);display:flex;align-items:center;gap:8px}
.brand .dot{width:14px;height:14px;background:var(--green);border-radius:50%}
.nav{position:absolute;top:42px;left:0;width:1200px;height:28px}
.nav a{position:absolute;top:4px;color:var(--white);text-decoration:none;font-size:13.5px;font-weight:500;white-space:nowrap}
.nav .pill{top:-3px;height:32px;border:2px solid var(--blue);border-radius:16px;text-align:center;line-height:28px}
.nav .pill.green{border-color:var(--green)}
.play{position:absolute;left:558px;top:228px;width:84px;height:84px;border:3px solid var(--white);border-radius:50%}
.hero h1{position:absolute;top:318px;left:0;width:1200px;text-align:center;color:var(--white);font-size:48px;font-weight:700}
.chev{position:absolute}
.wave{position:absolute;left:0;top:520px}

/* plans */
.plans{position:absolute;left:0;top:606px;width:1200px;height:712px;background:var(--plan-bg)}
.section-title{position:absolute;left:0;width:1200px;text-align:center;font-size:32px;font-weight:600;color:var(--ink)}
.lead{position:absolute;left:0;width:1200px;text-align:center;font-size:12.5px;line-height:21px;color:var(--muted)}
.plan{position:absolute;top:242px;width:266px;height:351px;background:var(--white);border-radius:22px;text-align:center;box-shadow:0 2px 8px rgba(0,0,0,.05)}
.plan .intro{margin-top:38px;font-family:Montserrat,sans-serif;font-size:16px;line-height:21px;color:#555}
.plan .price{margin-top:14px;font-family:Montserrat,sans-serif;font-weight:700;font-size:24px;color:var(--blue)}
.plan .price small{font-size:11px;color:var(--ink);font-weight:600}
.plan ul{list-style:none;margin-top:25px;font-size:12px;line-height:27.5px;color:#333}
.btn{display:inline-block;border:2px solid var(--blue);border-radius:20px;color:var(--blue);font-weight:600;font-size:14px;height:38px;line-height:34px;width:128px;margin-top:18px}

/* services */
.services{position:absolute;left:0;top:1318px;width:1200px;height:534px;background:var(--white)}
.service{position:absolute;top:200px;width:190px;text-align:center}
.service svg{display:block;margin:0 auto}
.service h3{margin-top:20px;font-size:18px;font-weight:600;line-height:29px;color:var(--ink)}
.service p{margin-top:16px;font-size:12px;line-height:21px;color:#333}
.dots{position:absolute;top:456px;left:559px;display:flex;gap:12px}
.dots span{width:11px;height:11px;border-radius:50%;background:#d3d3d3}
.dots span.on{background:var(--blue)}

/* live */
.live{position:absolute;left:0;top:1852px;width:1200px;height:505px;background:var(--grey-band)}
.live h2{position:absolute;left:172px;top:96px;font-size:32px;font-weight:600;line-height:37px}
.live .strong{position:absolute;left:172px;top:191px;font-family:Montserrat,sans-serif;font-weight:600;font-size:17.5px;line-height:29px;white-space:nowrap}
.live .small{position:absolute;left:172px;top:320px;font-size:12px;line-height:21px;color:#333;white-space:nowrap}
.feature{position:absolute;left:450px;top:87px;width:433px;height:326px;background:radial-gradient(circle at 50% 35%,#9fc9ef 0%,#3c86d6 40%,#1f4c8a 100%)}
.thumb{position:absolute;left:897px;width:130px;height:101px}
.tag{position:absolute;background:#e0161c;color:var(--white);font-family:Montserrat,sans-serif;font-weight:700;font-size:10px;padding:2px 6px}
.feature .tag{left:22px;top:20px;font-size:14px;padding:5px 13px}

/* videos */
.videos{position:absolute;left:0;top:2357px;width:1200px;height:852px;background:var(--white)}
.card{position:absolute;width:264px}
.card .img{position:relative;height:168px}
.card .img svg{position:absolute;right:24px;bottom:20px}
.card h4{margin-top:14px;font-size:17px;font-weight:600;line-height:23px;color:var(--ink)}
.card a{display:block;margin-top:6px;font-family:Montserrat,sans-serif;font-weight:600;font-size:12.5px;color:var(--blue);text-decoration:none}

/* footer */
.footer{position:absolute;left:0;top:3209px;width:1200px;height:421px;background:var(--black);color:var(--white)}
.footer h4{position:absolute;font-size:18px;font-weight:600}
.footer h4::after{content:"";position:absolute;left:0;top:34px;width:102px;height:2px;background:linear-gradient(90deg,var(--blue),var(--green))}
.footer ul{position:absolute;list-style:none;font-size:11.5px;line-height:24.6px;color:#ddd}
.field{position:absolute;font-size:12px;color:#eee;border-bottom:1px solid #555;width:185px;height:30px}
.social{position:absolute;top:3530px;display:flex;gap:8px;left:406px}
.social span{width:28px;height:28px;border:2px solid var(--white);border-radius:50%}
.submit{position:absolute;left:632px;top:3531px;width:89px;height:38px;border:2px solid var(--green);border-radius:19px;color:var(--white);font-size:14px;font-family:Montserrat,sans-serif;font-weight:600;text-align:center;line-height:34px}
.bottom{position:absolute;left:0;top:3630px;width:1200px;height:92px;background:var(--bar)}
.bottom .copy{position:absolute;right:172px;top:38px;font-size:12px;color:#eee}
</style>
</head>
<body>

<header class="hero">
  <div class="hero-photo" role="img" aria-label="Dim photo of a family watching a film on a big screen in a dark room"></div>
  <div class="brand" style="left:159px;top:36px">Lumora.TV<span class="dot"></span></div>
  <nav class="nav">
    <a style="left:373px">Home</a>
    <a style="left:452px">Where To Watch</a>
    <a style="left:605px">Partner</a>
    <a style="left:703px">Blog</a>
    <a style="left:773px">Contact</a>
    <a class="pill" style="left:852px;width:86px">About</a>
    <a class="pill green" style="left:947px;width:80px">Email</a>
  </nav>
  <div class="play">
    <svg width="78" height="78" viewBox="0 0 78 78"><defs><linearGradient id="pg" x1="0" y1="0" x2="1" y2="1"><stop offset="0" stop-color="#1e8fd5"/><stop offset="1" stop-color="#8dc63f"/></linearGradient></defs><path d="M30 24 L54 39 L30 54 Z" fill="url(#pg)"/></svg>
  </div>
  <h1>Lumora.TV Coming Soon</h1>
  <svg class="chev" style="left:34px;top:278px" width="34" height="68" viewBox="0 0 34 68"><path d="M32 2 L2 34 L32 66" fill="none" stroke="#fff" stroke-width="2"/></svg>
  <svg class="chev" style="left:1120px;top:278px" width="34" height="68" viewBox="0 0 34 68"><path d="M2 2 L32 34 L2 66" fill="none" stroke="#fff" stroke-width="2"/></svg>
  <svg class="wave" width="1200" height="120" viewBox="0 0 1200 120" preserveAspectRatio="none">
    <path d="M0 14 C150 90 300 115 500 108 C800 92 1000 40 1200 16 L1200 120 L0 120 Z" fill="#1e8fd5"/>
    <path d="M560 104 C800 88 1000 40 1200 16 L1200 50 C1000 62 820 88 620 104 Z" fill="#8dc63f"/>
    <path d="M0 52 C150 104 300 118 500 112 C800 98 1000 62 1200 50 L1200 120 L0 120 Z" fill="#e9e9e9"/>
  </svg>
</header>

<section class="plans">
  <h2 class="section-title" style="top:104px">Select Your Plan</h2>
  <p class="lead" style="top:166px">Lorem ipsum dolor sit amet, consectetur adipiscing elit, sed do eiusmod tempor iididunt<br>et dolore magna aliqua. Ut enim ad minim veniam, quis nostrud exercitalamco</p>
  <div class="plan" style="left:313px">
    <p class="intro">Get 1 month free,<br>then starts at</p>
    <p class="price">$5.99/ <small>month</small></p>
    <ul><li>Lorem ipsum dolor sit amet</li><li>Consectetur adipiscing elit</li><li>Do eiusmod tempor incididu</li><li>Sdolore magna aliqua.</li></ul>
    <span class="btn">Subscribe</span>
  </div>
  <div class="plan" style="left:621px">
    <p class="intro">Get 7 days free,<br>then starts at</p>
    <p class="price">$54.99/ <small>month</small></p>
    <ul><li>Lorem ipsum dolor sit amet</li><li>Consectetur adipiscing elit</li><li>Do eiusmod tempor incididu</li><li>Sdolore magna aliqua.</li></ul>
    <span class="btn">Subscribe</span>
  </div>
</section>

<section class="services">
  <h2 class="section-title" style="top:56px">Services</h2>
  <p class="lead" style="top:118px">Lorem ipsum dolor sit amet, consectetur adipiscing elit, sed do eiusmod tempor iididunt<br>et dolore magna aliqua. Ut enim ad minim veniam, quis nostrud exercitalamco</p>
  <div class="service" style="left:163px">
    <svg width="56" height="56" viewBox="0 0 56 56"><g fill="none" stroke="#333" stroke-width="2"><circle cx="28" cy="28" r="16"/><circle cx="28" cy="28" r="6"/></g><path d="M28 6v6M28 44v6M6 28h6M44 28h6M12 12l5 5M39 39l5 5M44 12l-5 5M17 39l-5 5" stroke="#333" stroke-width="5"/><path d="M28 12 A16 16 0 0 1 44 28 L34 28 A6 6 0 0 0 28 22Z" fill="#8dc63f"/></svg>
    <h3>Lorem ipm<br>losite loectetur</h3>
    <p>Lorem ipsum dolor sit amtns<br>ecte sed do eiusmod temritolre<br>magna am ad minimn.</p>
  </div>
  <div class="service" style="left:390px">
    <svg width="56" height="56" viewBox="0 0 56 56"><circle cx="18" cy="18" r="12" fill="none" stroke="#333" stroke-width="2"/><circle cx="18" cy="18" r="4" fill="none" stroke="#333" stroke-width="2"/><path d="M26 26 L48 48 M40 40 l-5 5 M46 46 l-4 4" stroke="#8dc63f" stroke-width="5" stroke-linecap="round"/></svg>
    <h3>Lorem ipm<br>losite loectetur</h3>
    <p>Lorem ipsum dolor sit amtns<br>ecte sed do eiusmod temritolre<br>magna am ad minimn.</p>
  </div>
  <div class="service" style="left:617px">
    <svg width="56" height="56" viewBox="0 0 56 56"><circle cx="28" cy="16" r="10" fill="#8dc63f" stroke="#333" stroke-width="2"/><path d="M6 52 C6 34 50 34 50 52 Z" fill="#1e8fd5" stroke="#333" stroke-width="2"/></svg>
    <h3>Lorem ipm<br>losite loectetur</h3>
    <p>Lorem ipsum dolor sit amtns<br>ecte sed do eiusmod temritolre<br>magna am ad minimn.</p>
  </div>
  <div class="service" style="left:844px">
    <svg width="56" height="56" viewBox="0 0 56 56"><path d="M28 2v52" stroke="#333" stroke-width="2"/><path d="M40 14 C36 8 18 8 18 18 C18 28 40 26 40 38 C40 48 20 48 16 42" fill="none" stroke="#8dc63f" stroke-width="5"/></svg>
    <h3>Lorem ipm<br>losite loectetur</h3>
    <p>Lorem ipsum dolor sit amtns<br>ecte sed do eiusmod temritolre<br>magna am ad minimn.</p>
  </div>
  <div class="dots"><span class="on"></span><span></span><span></span><span></span></div>
</section>

<section class="live">
  <h2>Live TV<br>Channels</h2>
  <p class="strong">Lorem ipsum dolor sit aet<br>cons ectetur adipiscing lit<br>sed do eius mod temporn<br>cididunt ut labor.</p>
  <p class="small">Lorem ipsum dolor sit amet, consected<br>iscing t, sed do eiusmod tempor iidtolore<br>magna am ad minim veniam, str.</p>
  <svg class="chev" style="left:102px;top:232px" width="22" height="42" viewBox="0 0 22 42"><path d="M20 1 L2 21 L20 41" fill="none" stroke="#444" stroke-width="1.5"/></svg>
  <svg class="chev" style="left:1068px;top:232px" width="22" height="42" viewBox="0 0 22 42"><path d="M2 1 L20 21 L2 41" fill="none" stroke="#444" stroke-width="1.5"/></svg>
  <div class="feature" role="img" aria-label="News presenter in a suit on a blue studio set"><span class="tag">LIVE</span></div>
  <div class="thumb" style="top:87px;background:linear-gradient(160deg,#3a7fc6,#122a55)" role="img" aria-label="Grid of channel tiles on a TV screen"><span class="tag" style="left:12px;top:8px">LIVE</span></div>
  <div class="thumb" style="top:199px;background:linear-gradient(180deg,#6a8f4a,#3f6a2a)" role="img" aria-label="Football players competing for the ball"><span class="tag" style="left:12px;top:8px">LIVE</span></div>
  <div class="thumb" style="top:311px;background:linear-gradient(180deg,#3a3a8a,#1a1030 60%,#c46a2a)" role="img" aria-label="Concert crowd under stage lights"><span class="tag" style="left:12px;top:8px">LIVE</span></div>
</section>

<section class="videos">
  <h2 class="section-title" style="top:74px">Videos</h2>
  <p class="lead" style="top:136px">Lorem ipsum dolor sit amet, consectetur adipiscing elit, sed do eiusmod tempor iididunt<br>et dolore magna aliqua. Ut enim ad minim veniam, quis nostrud exercitalamco</p>
  <svg class="chev" style="left:102px;top:412px" width="22" height="42" viewBox="0 0 22 42"><path d="M20 1 L2 21 L20 41" fill="none" stroke="#444" stroke-width="1.5"/></svg>
  <svg class="chev" style="left:1068px;top:412px" width="22" height="42" viewBox="0 0 22 42"><path d="M2 1 L20 21 L2 41" fill="none" stroke="#444" stroke-width="1.5"/></svg>

  <article class="card" style="left:173px;top:203px">
    <div class="img" role="img" aria-label="Animated film still with a city at night" style="background:linear-gradient(135deg,#2b5a86,#c9a24a)"><svg width="26" height="26" viewBox="0 0 26 26"><circle cx="13" cy="13" r="12" fill="none" stroke="#fff" stroke-width="1.5"/><path d="M10 8 L18 13 L10 18Z" fill="#3aa58c"/></svg></div>
    <h4>Sed ut perspiciatis ulonde<br>omnis te natus error lorsit<br>volupersplc lorem.</h4><a>Read More</a>
  </article>
  <article class="card" style="left:469px;top:203px">
    <div class="img" role="img" aria-label="Hockey team on a field at sunset" style="background:linear-gradient(180deg,#c9c3b3,#5a6a48)"><svg width="26" height="26" viewBox="0 0 26 26"><circle cx="13" cy="13" r="12" fill="none" stroke="#fff" stroke-width="1.5"/><path d="M10 8 L18 13 L10 18Z" fill="#3aa58c"/></svg></div>
    <h4>Sed ut perspiciatis ulonde<br>omnis te natus error lorsit<br>volupersplc lorem.</h4><a>Read More</a>
  </article>
  <article class="card" style="left:762px;top:203px">
    <div class="img" role="img" aria-label="Friends cheering in front of a TV" style="background:linear-gradient(135deg,#4a3a3a,#1e2226)"><svg width="26" height="26" viewBox="0 0 26 26"><circle cx="13" cy="13" r="12" fill="none" stroke="#fff" stroke-width="1.5"/><path d="M10 8 L18 13 L10 18Z" fill="#3aa58c"/></svg></div>
    <h4>Sed ut perspiciatis ulonde<br>omnis te natus error lorsit<br>volupersplc lorem.</h4><a>Read More</a>
  </article>

  <article class="card" style="left:173px;top:511px">
    <div class="img" role="img" aria-label="Vintage film projector beaming light in the dark" style="background:radial-gradient(circle at 70% 40%,#a58a5a,#111 55%)"><svg width="26" height="26" viewBox="0 0 26 26"><circle cx="13" cy="13" r="12" fill="none" stroke="#fff" stroke-width="1.5"/><path d="M10 8 L18 13 L10 18Z" fill="#3aa58c"/></svg></div>
    <h4>Sed ut perspiciatis ulonde<br>omnis te natus error lorsit<br>volupersplc lorem.</h4><a>Read More</a>
  </article>
  <article class="card" style="left:469px;top:511px">
    <div class="img" role="img" aria-label="Father and child on a sofa with a remote" style="background:linear-gradient(135deg,#9a9a9a,#3a3a3a)"><svg width="26" height="26" viewBox="0 0 26 26"><circle cx="13" cy="13" r="12" fill="none" stroke="#fff" stroke-width="1.5"/><path d="M10 8 L18 13 L10 18Z" fill="#3aa58c"/></svg></div>
    <h4>Sed ut perspiciatis ulonde<br>omnis te natus error lorsit<br>volupersplc lorem.</h4><a>Read More</a>
  </article>
  <article class="card" style="left:762px;top:511px">
    <div class="img" role="img" aria-label="Cartoon monsters at a holiday party" style="background:linear-gradient(180deg,#2a3f8a,#5a2a7a)"><svg width="26" height="26" viewBox="0 0 26 26"><circle cx="13" cy="13" r="12" fill="none" stroke="#fff" stroke-width="1.5"/><path d="M10 8 L18 13 L10 18Z" fill="#3aa58c"/></svg></div>
    <h4>Sed ut perspiciatis ulonde<br>omnis te natus error lorsit<br>volupersplc lorem.</h4><a>Read More</a>
  </article>
</section>

<footer class="footer">
  <h4 style="left:173px;top:76px">Live Shows</h4>
  <ul style="left:173px;top:126px"><li>Lorem ipsum dor smet</li><li>Consectetur adipisc</li><li>Sed do eiusmod tempor</li><li>Kncididunt ut labore et</li><li>Dolore magna aliqua.</li><li>Ut enim ad mm veniam</li><li>Quis nostrud extation</li><li>Wllamco laboris nisi ut</li><li>Aliquip ex emod</li></ul>
  <h4 style="left:406px;top:76px">Links</h4>
  <ul style="left:406px;top:126px"><li>Lorem ipsum dolor si</li><li>Kncididunt ut labore et</li><li>Dolore magna aliqua.</li><li>Ut enim ad mive</li></ul>
  <h4 style="left:406px;top:271px">Follow</h4>
  <h4 style="left:632px;top:76px">Contact Form</h4>
  <div class="field" style="left:632px;top:145px">Name:</div>
  <div class="field" style="left:845px;top:145px">Email:</div>
  <div class="field" style="left:632px;top:197px">Phone:</div>
  <div class="field" style="left:845px;top:197px">Subject:</div>
  <div class="field" style="left:632px;top:235px;width:398px;height:62px">Message:</div>
</footer>
<div class="social" aria-label="Social links"><span></span><span></span><span></span><span></span></div>
<div class="submit">Submit</div>

<div class="bottom">
  <div class="brand" style="left:173px;top:26px">Lumora.TV<span class="dot"></span></div>
  <p class="copy">© 2020 Lumora.TV. All Rights are reserved.</p>
</div>
</body>
</html>
```